Jewelry store needs fully functional Ecommerce website

Web Design Brief for our E-commerce Jewelry retail store.
Description

We need a fully coded Shopify website. The Shopify site will need to be fully functional with an Ecommerce integration (fully integrated with Paypal and All other gateways) and will need to be SEO optimized.
We sell jewelry items like: rings, earrings, necklaces etc. The website should have an elegant, modern, professional, fun, look.

***We would like the website to look and function similarly to this website:
https://velvorisco.com

Color Preference
Colors to be used are white background with black font and light pink/ purple/ gold tints. We have attached our logo as reference.

Functionalities
The store will function like a typical Ecommerce jewelry store, using the products/categories as the starting page. Going into individual product pages by selecting images and leading to a detailed “buy now” page for the selected product.

Target Market
Jewelry lovers.

Should Not Have:
- - Dull and common design
- - Messy/unstructured navigation

Coded - Design and coding required
Target Audience are women from 16-50 years old.
We will need to be able to add products and make modifications to the website as needed.

We need the following apps installed and Operating:
-Tally Shift; Order Look Up (rename “track your order”) ; Help Center (Questions and Answers) ; Pemmo Reviews; TXT Nudge; Drenoza Email Marketing ; Plivet (Facebook messenger bump) ; Vantro multi- currency (translate currency to buyer) ; Discounted Upsell ; Easy Contact form App
We will need all products imported: (below is information for importing products). We will provide all links that serve entire active item product catalog in shopifys import format:
DataFeed:

If you are getting started with Shopify, a combination of the Shopify Import Format and XML feeds is ideal. The Shopify Import Format will output a file that can be uploaded into Shopify’s product database. After you import, you can use the XML feed and a third party app to keep the inventory up to date in real time, take down items that go out of stock etc., all without regular human intervention. There a several Shopify apps that can do this type of feed integration. We have had a good experience with Tally Shift, which is an app that can be configured to accept our XML feed and update products on a set schedule. You can even set your own margins based on our wholesale price with this app.

Shopify Formatted HTML TableTo make it easier to get started on Shopify, we included a format that outputs the required fields for a product import in Shopify. In order to use the embedded Excel file, first open the file (Auto-Shopify-Datasheet-Format.xslx), Refresh it (under Data tab), and then Save As with a new file name in a CSV (UTF-8) file. That file can then be split into smaller CSV files (if there is a limit on the number of products per file) for import into Shopify.

Target Market(s)

Jewelry Lovers

Industry/Entity Type

Jewelry Store

Coding

Number of Pages Required

5+ page

Colors
eda3c7
d3a5cc
ffffff

Requirements
Must have
• Color Preference
Colors to be used are white background with black font and light pink/ purple/ gold tints.

https://velvorisco.com
Should not have
• Should Not Have:

```html
<!DOCTYPE html>
<html lang="en">
<head>
<meta charset="utf-8">
<title>Lumen Vow — Jewelry Store</title>
<link href="https://fonts.googleapis.com/css2?family=Poppins:wght@300;400;500;600&family=Gelasio:wght@600&family=Roboto:wght@300;700&display=swap" rel="stylesheet">
<style>
:root{
  --hero:#9b897d;
  --page:#f6f6f6;
  --white:#ffffff;
  --ink:#1c1c1c;
  --text:#444444;
  --muted:#8a8a8a;
  --line:#e6e6e6;
  --pink:#eaa3c7;
  --plum:#b4558a;
  --dark:#2c2c2c;
  --badge:#e88bb8;
}
*{box-sizing:border-box;margin:0;padding:0}
html,body{width:1200px;height:2954px;overflow:hidden}
body{position:relative;background:var(--page);font-family:"Poppins",sans-serif;color:var(--text)}
.abs{position:absolute}

/* hero */
.hero{left:0;top:0;width:1200px;height:521px;background:var(--hero)}
.hero-photo{left:206px;top:0;width:494px;height:521px;background:radial-gradient(ellipse at 50% 40%,#c9a58a 0%,#8f6c55 45%,rgba(155,137,125,0) 75%)}
.brand{left:0;top:0;width:213px;height:89px;background:var(--white);display:flex;flex-direction:column;align-items:center;justify-content:center;gap:6px}
.brand-name{font-size:24px;font-weight:400;color:#3a3a3a;letter-spacing:1px}
.brand-sub{font-size:9px;font-weight:400;color:#c6a96c;letter-spacing:2px}
.nav{top:30px;left:690px;display:flex;gap:0;align-items:center}
.nav a{color:var(--white);text-decoration:none;font-size:17px;position:absolute;white-space:nowrap}
.cart{left:1068px;top:34px}
.cart-count{left:1079px;top:30px;width:17px;height:17px;border-radius:50%;background:var(--badge);color:var(--white);font-size:10px;display:flex;align-items:center;justify-content:center}
.hero-title{left:704px;top:190px;font-size:39px;font-weight:400;color:var(--white)}
.hero-copy{left:705px;top:246px;width:300px;font-size:14.5px;line-height:22px;color:var(--white)}
.hero-btn{left:706px;top:315px;width:159px;height:46px;border-radius:23px;background:var(--white);color:var(--ink);font-size:15px;display:flex;align-items:center;justify-content:center}

/* product cards */
.card{position:absolute;width:224px;height:283px;background:var(--white);border:1px solid var(--line)}
.card-media{height:194px}
.card-name{position:absolute;left:14px;top:206px;font-size:12.5px;font-weight:600;color:#333}
.card-brand{position:absolute;left:14px;top:229px;font-size:10.5px;color:var(--muted)}
.card-price{position:absolute;left:14px;top:250px;font-size:12px;color:var(--muted)}
.card-price b{font-weight:600;color:#555}
.card-heart{position:absolute;right:11px;top:208px}
.card-share{position:absolute;right:11px;top:243px}
.m-ring{background:linear-gradient(135deg,#f1f0ef,#dedcd9 60%,#cfc9c2)}
.m-chain{background:linear-gradient(135deg,#dcdcdb,#c4c3c0 55%,#d8d2c3)}
.m-ear{background:linear-gradient(135deg,#5a3f35,#2e1f1c 60%,#1b1414)}
.m-neck{background:linear-gradient(135deg,#4e4340,#7e5a48 55%,#3a302d)}

/* pagination */
.pager{left:0;top:1578px;width:1200px;display:flex;justify-content:center;gap:8px}
.pager span{width:25px;height:25px;background:var(--white);border:1px solid var(--line);font-size:12px;color:#333;display:flex;align-items:center;justify-content:center}

/* recent */
.recent-title{left:0;top:1683px;width:1200px;text-align:center;font-family:"Gelasio",serif;font-weight:600;font-size:20px;color:#3a3a3a;letter-spacing:.3px}
.recent-copy{left:290px;top:1721px;width:620px;text-align:center;font-size:14px;line-height:21px;color:#6e6e6e}
.slide-arrow{width:25px;height:23px;background:#3d4451;display:flex;align-items:center;justify-content:center}

/* promo */
.promo{left:0;top:2170px;width:1200px;height:422px;background:var(--pink)}
.promo-kicker{left:111px;top:2254px;font-family:"Roboto",sans-serif;font-weight:300;font-size:36px;color:var(--ink)}
.promo-head{left:109px;top:2296px;font-family:"Roboto",sans-serif;font-weight:700;font-size:72px;letter-spacing:-2px;color:var(--ink)}
.promo-copy{left:612px;top:2255px;width:420px;font-size:13.5px;line-height:25px;color:#2a2a2a}
.promo-input{left:612px;top:2314px;width:392px;height:49px;background:var(--white);font-size:12px;color:#b9b9b9;padding-left:17px;display:flex;align-items:center}
.promo-send{left:1004px;top:2314px;width:82px;height:49px;background:var(--plum);display:flex;align-items:center;justify-content:center}

/* gallery */
.gallery{left:112px;top:2397px;width:974px;height:390px;display:grid;grid-template-columns:repeat(5,1fr);grid-template-rows:repeat(2,1fr)}
.g1{background:linear-gradient(135deg,#d8c3b0,#a7806a)}
.g2{background:linear-gradient(135deg,#c81f3e,#e9d3cf 55%,#c81f3e)}
.g3{background:linear-gradient(135deg,#e5e3df,#9a9894 70%,#5e5d5b)}
.g4{background:linear-gradient(135deg,#c9c9c9,#4b6f6e 60%,#2f4b4c)}
.g5{background:linear-gradient(135deg,#6f6358,#a88066 55%,#4d433b)}
.g6{background:linear-gradient(135deg,#d9c3ad,#a4775c)}
.g7{background:linear-gradient(135deg,#6a6a6a,#3d2b26 55%,#8c8c8c)}
.g8{background:linear-gradient(135deg,#e2e0dc,#8e8c88 70%,#53524f)}
.g9{background:linear-gradient(135deg,#b9c1c9,#d7ab93 55%,#e9dfd6)}
.g10{background:linear-gradient(135deg,#6e6358,#a7806a 55%,#4a4039)}

/* footer */
.footer{left:0;top:2871px;width:1200px;height:83px;background:var(--dark)}
.copyright{left:112px;top:2904px;font-size:10.5px;color:var(--white)}
.footer-links{left:0;top:2904px;width:1086px;display:flex;justify-content:flex-end;gap:12px;font-size:10.5px;color:var(--white)}
</style>
</head>
<body>

<header>
  <div class="abs hero"></div>
  <div class="abs hero-photo" role="img" aria-label="Portrait of a model with long wavy hair wearing gold earrings"></div>
  <div class="abs brand"><span class="brand-name">Lumen Vow</span><span class="brand-sub">BY MARA AND TESS</span></div>
  <nav>
    <a class="abs" style="left:690px;top:32px;color:#fff;font-size:17px;text-decoration:none">Home</a>
    <a class="abs" style="left:780px;top:32px;color:#fff;font-size:17px;text-decoration:none">Shop</a>
    <a class="abs" style="left:862px;top:32px;color:#fff;font-size:17px;text-decoration:none">Featured</a>
    <a class="abs" style="left:976px;top:32px;color:#fff;font-size:17px;text-decoration:none">Contact</a>
  </nav>
  <svg class="abs cart" width="18" height="18" viewBox="0 0 24 24" fill="#fff"><path d="M1 3h4l2.6 11.2h11.6L22 6H7"/><path d="M7 6h15l-2.8 8.2H7.6z"/><circle cx="9" cy="20" r="2"/><circle cx="18" cy="20" r="2"/></svg>
  <div class="abs cart-count">4</div>
  <h1 class="abs hero-title">Online Shopping</h1>
  <p class="abs hero-copy">Lorem Ipsum is simply dummy text of the printing and typesetting industry.</p>
  <div class="abs hero-btn">Learn More</div>
</header>

<main>
  <section class="products">
    <!-- row 1 -->
    <div class="card" style="left:112px;top:627px"><div class="card-media m-ring" role="img" aria-label="Stacked gold rings with pink stones"></div><div class="card-name">Product Name</div><div class="card-brand">Brand Name will be Here</div><div class="card-price">Price: <b>$250</b></div><svg class="card-heart" width="12" height="11" viewBox="0 0 24 22" fill="#999"><path d="M12 21 2.5 11.6A5.6 5.6 0 0 1 12 3.7a5.6 5.6 0 0 1 9.5 7.9z"/></svg><svg class="card-share" width="11" height="11" viewBox="0 0 24 24" fill="#999"><circle cx="18" cy="5" r="3"/><circle cx="6" cy="12" r="3"/><circle cx="18" cy="19" r="3"/><path d="M8 11l8-5M8 13l8 5" stroke="#999" stroke-width="2"/></svg></div>
    <div class="card" style="left:362px;top:627px"><div class="card-media m-chain" role="img" aria-label="Gold link chain on stone"></div><div class="card-name">Product Name</div><div class="card-brand">Brand Name will be Here</div><div class="card-price">Price: <b>$170</b></div><svg class="card-heart" width="12" height="11" viewBox="0 0 24 22" fill="#999"><path d="M12 21 2.5 11.6A5.6 5.6 0 0 1 12 3.7a5.6 5.6 0 0 1 9.5 7.9z"/></svg><svg class="card-share" width="11" height="11" viewBox="0 0 24 24" fill="#999"><circle cx="18" cy="5" r="3"/><circle cx="6" cy="12" r="3"/><circle cx="18" cy="19" r="3"/><path d="M8 11l8-5M8 13l8 5" stroke="#999" stroke-width="2"/></svg></div>
    <div class="card" style="left:612px;top:627px"><div class="card-media m-ear" role="img" aria-label="Gold hoop earrings worn on an ear"></div><div class="card-name">Product Name</div><div class="card-brand">Brand Name will be Here</div><div class="card-price">Price: <b>$227</b></div><svg class="card-heart" width="12" height="11" viewBox="0 0 24 22" fill="#999"><path d="M12 21 2.5 11.6A5.6 5.6 0 0 1 12 3.7a5.6 5.6 0 0 1 9.5 7.9z"/></svg><svg class="card-share" width="11" height="11" viewBox="0 0 24 24" fill="#999"><circle cx="18" cy="5" r="3"/><circle cx="6" cy="12" r="3"/><circle cx="18" cy="19" r="3"/><path d="M8 11l8-5M8 13l8 5" stroke="#999" stroke-width="2"/></svg></div>
    <div class="card" style="left:862px;top:627px"><div class="card-media m-neck" role="img" aria-label="Gold charm necklaces held in a hand"></div><div class="card-name">Product Name</div><div class="card-brand">Brand Name will be Here</div><div class="card-price">Price: <b>$277</b></div><svg class="card-heart" width="12" height="11" viewBox="0 0 24 22" fill="#999"><path d="M12 21 2.5 11.6A5.6 5.6 0 0 1 12 3.7a5.6 5.6 0 0 1 9.5 7.9z"/></svg><svg class="card-share" width="11" height="11" viewBox="0 0 24 24" fill="#999"><circle cx="18" cy="5" r="3"/><circle cx="6" cy="12" r="3"/><circle cx="18" cy="19" r="3"/><path d="M8 11l8-5M8 13l8 5" stroke="#999" stroke-width="2"/></svg></div>
    <!-- row 2 -->
    <div class="card" style="left:112px;top:942px"><div class="card-media m-ring" role="img" aria-label="Stacked gold rings with pink stones"></div><div class="card-name">Product Name</div><div class="card-brand">Brand Name will be Here</div><div class="card-price">Price: <b>$250</b></div><svg class="card-heart" width="12" height="11" viewBox="0 0 24 22" fill="#999"><path d="M12 21 2.5 11.6A5.6 5.6 0 0 1 12 3.7a5.6 5.6 0 0 1 9.5 7.9z"/></svg><svg class="card-share" width="11" height="11" viewBox="0 0 24 24" fill="#999"><circle cx="18" cy="5" r="3"/><circle cx="6" cy="12" r="3"/><circle cx="18" cy="19" r="3"/><path d="M8 11l8-5M8 13l8 5" stroke="#999" stroke-width="2"/></svg></div>
    <div class="card" style="left:362px;top:942px"><div class="card-media m-chain" role="img" aria-label="Gold link chain on stone"></div><div class="card-name">Product Name</div><div class="card-brand">Brand Name will be Here</div><div class="card-price">Price: <b>$170</b></div><svg class="card-heart" width="12" height="11" viewBox="0 0 24 22" fill="#999"><path d="M12 21 2.5 11.6A5.6 5.6 0 0 1 12 3.7a5.6 5.6 0 0 1 9.5 7.9z"/></svg><svg class="card-share" width="11" height="11" viewBox="0 0 24 24" fill="#999"><circle cx="18" cy="5" r="3"/><circle cx="6" cy="12" r="3"/><circle cx="18" cy="19" r="3"/><path d="M8 11l8-5M8 13l8 5" stroke="#999" stroke-width="2"/></svg></div>
    <div class="card" style="left:612px;top:942px"><div class="card-media m-ear" role="img" aria-label="Gold hoop earrings worn on an ear"></div><div class="card-name">Product Name</div><div class="card-brand">Brand Name will be Here</div><div class="card-price">Price: <b>$227</b></div><svg class="card-heart" width="12" height="11" viewBox="0 0 24 22" fill="#999"><path d="M12 21 2.5 11.6A5.6 5.6 0 0 1 12 3.7a5.6 5.6 0 0 1 9.5 7.9z"/></svg><svg class="card-share" width="11" height="11" viewBox="0 0 24 24" fill="#999"><circle cx="18" cy="5" r="3"/><circle cx="6" cy="12" r="3"/><circle cx="18" cy="19" r="3"/><path d="M8 11l8-5M8 13l8 5" stroke="#999" stroke-width="2"/></svg></div>
    <div class="card" style="left:862px;top:942px"><div class="card-media m-neck" role="img" aria-label="Gold charm necklaces held in a hand"></div><div class="card-name">Product Name</div><div class="card-brand">Brand Name will be Here</div><div class="card-price">Price: <b>$277</b></div><svg class="card-heart" width="12" height="11" viewBox="0 0 24 22" fill="#999"><path d="M12 21 2.5 11.6A5.6 5.6 0 0 1 12 3.7a5.6 5.6 0 0 1 9.5 7.9z"/></svg><svg class="card-share" width="11" height="11" viewBox="0 0 24 24" fill="#999"><circle cx="18" cy="5" r="3"/><circle cx="6" cy="12" r="3"/><circle cx="18" cy="19" r="3"/><path d="M8 11l8-5M8 13l8 5" stroke="#999" stroke-width="2"/></svg></div>
    <!-- row 3 -->
    <div class="card" style="left:112px;top:1257px"><div class="card-media m-ring" role="img" aria-label="Stacked gold rings with pink stones"></div><div class="card-name">Product Name</div><div class="card-brand">Brand Name will be Here</div><div class="card-price">Price: <b>$250</b></div><svg class="card-heart" width="12" height="11" viewBox="0 0 24 22" fill="#999"><path d="M12 21 2.5 11.6A5.6 5.6 0 0 1 12 3.7a5.6 5.6 0 0 1 9.5 7.9z"/></svg><svg class="card-share" width="11" height="11" viewBox="0 0 24 24" fill="#999"><circle cx="18" cy="5" r="3"/><circle cx="6" cy="12" r="3"/><circle cx="18" cy="19" r="3"/><path d="M8 11l8-5M8 13l8 5" stroke="#999" stroke-width="2"/></svg></div>
    <div class="card" style="left:362px;top:1257px"><div class="card-media m-chain" role="img" aria-label="Gold link chain on stone"></div><div class="card-name">Product Name</div><div class="card-brand">Brand Name will be Here</div><div class="card-price">Price: <b>$170</b></div><svg class="card-heart" width="12" height="11" viewBox="0 0 24 22" fill="#999"><path d="M12 21 2.5 11.6A5.6 5.6 0 0 1 12 3.7a5.6 5.6 0 0 1 9.5 7.9z"/></svg><svg class="card-share" width="11" height="11" viewBox="0 0 24 24" fill="#999"><circle cx="18" cy="5" r="3"/><circle cx="6" cy="12" r="3"/><circle cx="18" cy="19" r="3"/><path d="M8 11l8-5M8 13l8 5" stroke="#999" stroke-width="2"/></svg></div>
    <div class="card" style="left:612px;top:1257px"><div class="card-media m-ear" role="img" aria-label="Gold hoop earrings worn on an ear"></div><div class="card-name">Product Name</div><div class="card-brand">Brand Name will be Here</div><div class="card-price">Price: <b>$227</b></div><svg class="card-heart" width="12" height="11" viewBox="0 0 24 22" fill="#999"><path d="M12 21 2.5 11.6A5.6 5.6 0 0 1 12 3.7a5.6 5.6 0 0 1 9.5 7.9z"/></svg><svg class="card-share" width="11" height="11" viewBox="0 0 24 24" fill="#999"><circle cx="18" cy="5" r="3"/><circle cx="6" cy="12" r="3"/><circle cx="18" cy="19" r="3"/><path d="M8 11l8-5M8 13l8 5" stroke="#999" stroke-width="2"/></svg></div>
    <div class="card" style="left:862px;top:1257px"><div class="card-media m-neck" role="img" aria-label="Gold charm necklaces held in a hand"></div><div class="card-name">Product Name</div><div class="card-brand">Brand Name will be Here</div><div class="card-price">Price: <b>$277</b></div><svg class="card-heart" width="12" height="11" viewBox="0 0 24 22" fill="#999"><path d="M12 21 2.5 11.6A5.6 5.6 0 0 1 12 3.7a5.6 5.6 0 0 1 9.5 7.9z"/></svg><svg class="card-share" width="11" height="11" viewBox="0 0 24 24" fill="#999"><circle cx="18" cy="5" r="3"/><circle cx="6" cy="12" r="3"/><circle cx="18" cy="19" r="3"/><path d="M8 11l8-5M8 13l8 5" stroke="#999" stroke-width="2"/></svg></div>
  </section>

  <div class="abs pager">
    <span><svg width="8" height="8" viewBox="0 0 10 10"><path d="M7 1 3 5l4 4" fill="none" stroke="#222" stroke-width="2"/></svg></span>
    <span>1</span><span>2</span><span>3</span><span>4</span>
    <span><svg width="8" height="8" viewBox="0 0 10 10"><path d="M3 1l4 4-4 4" fill="none" stroke="#222" stroke-width="2"/></svg></span>
  </div>

  <section class="recent">
    <h2 class="abs recent-title">Recently You Have Viewed</h2>
    <p class="abs recent-copy">Lorem ipsum dolor sit amet, consectetur adipisicing eiusmod tempor incididunt ut labore et consectetur adipisicing eiusmod dolore magna aliqua.</p>
    <div class="abs slide-arrow" style="left:170px;top:1940px"><svg width="13" height="9" viewBox="0 0 14 10"><path d="M13 5H2M5 1 1 5l4 4" fill="none" stroke="#fff" stroke-width="1.8"/></svg></div>
    <div class="abs slide-arrow" style="left:1004px;top:1940px"><svg width="13" height="9" viewBox="0 0 14 10"><path d="M1 5h11M9 1l4 4-4 4" fill="none" stroke="#fff" stroke-width="1.8"/></svg></div>
    <div class="card" style="left:237px;top:1811px"><div class="card-media m-ring" role="img" aria-label="Stacked gold rings with pink stones"></div><div class="card-name">Product Name</div><div class="card-brand">Brand Name will be Here</div><div class="card-price">Price: <b>$199</b></div><svg class="card-heart" width="12" height="11" viewBox="0 0 24 22" fill="#999"><path d="M12 21 2.5 11.6A5.6 5.6 0 0 1 12 3.7a5.6 5.6 0 0 1 9.5 7.9z"/></svg><svg class="card-share" width="11" height="11" viewBox="0 0 24 24" fill="#999"><circle cx="18" cy="5" r="3"/><circle cx="6" cy="12" r="3"/><circle cx="18" cy="19" r="3"/><path d="M8 11l8-5M8 13l8 5" stroke="#999" stroke-width="2"/></svg></div>
    <div class="card" style="left:487px;top:1811px"><div class="card-media m-chain" role="img" aria-label="Gold link chain on stone"></div><div class="card-name">Product Name</div><div class="card-brand">Brand Name will be Here</div><div class="card-price">Price: <b>$207</b></div><svg class="card-heart" width="12" height="11" viewBox="0 0 24 22" fill="#999"><path d="M12 21 2.5 11.6A5.6 5.6 0 0 1 12 3.7a5.6 5.6 0 0 1 9.5 7.9z"/></svg><svg class="card-share" width="11" height="11" viewBox="0 0 24 24" fill="#999"><circle cx="18" cy="5" r="3"/><circle cx="6" cy="12" r="3"/><circle cx="18" cy="19" r="3"/><path d="M8 11l8-5M8 13l8 5" stroke="#999" stroke-width="2"/></svg></div>
    <div class="card" style="left:738px;top:1811px"><div class="card-media m-ear" role="img" aria-label="Gold hoop earrings worn on an ear"></div><div class="card-name">Product Name</div><div class="card-brand">Brand Name will be Here</div><div class="card-price">Price: <b>$29</b></div><svg class="card-heart" width="12" height="11" viewBox="0 0 24 22" fill="#999"><path d="M12 21 2.5 11.6A5.6 5.6 0 0 1 12 3.7a5.6 5.6 0 0 1 9.5 7.9z"/></svg><svg class="card-share" width="11" height="11" viewBox="0 0 24 24" fill="#999"><circle cx="18" cy="5" r="3"/><circle cx="6" cy="12" r="3"/><circle cx="18" cy="19" r="3"/><path d="M8 11l8-5M8 13l8 5" stroke="#999" stroke-width="2"/></svg></div>
  </section>

  <section class="promo-section">
    <div class="abs promo"></div>
    <div class="abs promo-kicker">GET 10% OFF YOUR</div>
    <div class="abs promo-head">FIRST ORDER</div>
    <p class="abs promo-copy">As a welcome to all our new customers we have a special code which you can use to get 10% off your first order.</p>
    <div class="abs promo-input">Email address</div>
    <div class="abs promo-send"><svg width="22" height="22" viewBox="0 0 24 24" fill="none" stroke="#fff" stroke-width="1.5"><path d="M21 3 3 10.5l8 2.5 2.5 8z"/></svg></div>
    <div class="abs gallery">
      <div class="g1" role="img" aria-label="Gold locket necklace held in hands"></div>
      <div class="g2" role="img" aria-label="Layered silver pendant necklaces on a red top"></div>
      <div class="g3" role="img" aria-label="Gold rings with colored stones on marble"></div>
      <div class="g4" role="img" aria-label="Silver chain bracelets on a wrist"></div>
      <div class="g5" role="img" aria-label="Hands wearing many gemstone rings"></div>
      <div class="g6" role="img" aria-label="Gold locket necklace held in hands"></div>
      <div class="g7" role="img" aria-label="Hand wearing a gold statement ring"></div>
      <div class="g8" role="img" aria-label="Gold rings with colored stones on marble"></div>
      <div class="g9" role="img" aria-label="Rose gold and silver disc pendants"></div>
      <div class="g10" role="img" aria-label="Hands wearing many gemstone rings"></div>
    </div>
  </section>
</main>

<footer>
  <div class="abs footer"></div>
  <div class="abs copyright">Copyright 2021 - All Right Reserved</div>
  <div class="abs footer-links"><span>Help</span><span>About</span><span>FAQ</span><span>Privacy</span><span>Contact</span><span>Term</span></div>
</footer>

</body>
</html>
```